KT Holloway Insurance Group, LLC - Branding Project

We have an existing business card that was designed on Quillmark Press. We recently completed a new logo design with sketch hive and would like to utilize this new logo design into a business card design. Our new logo will be a major emphasis of our branding that is currently under development.

We are an independent insurance agency licensed in Colorado. We specialized in four keys areas. Business Insurance, Risk Management, Employee Benefits and Investments.

We would like the efforts of this design to last for 5 years minimum. Existing business card and new logo design files attached.

Requirements
Must have
• My office is a virtual office. All of our marketing effort drive from the Denver, CO office location. Our mailing address is just for mailing, that's it.
• Please maintain the color scheme of the new logo design.
Nice to have
• Doublesided card, I think? Your the expert if you have other ideas that are better I am excited to see them.

```html
<!DOCTYPE html>
<html lang="en">
<head>
<meta charset="utf-8">
<title>KT Holloway Insurance Group – Business Card</title>
<link rel="stylesheet" href="https://fonts.googleapis.com/css2?family=Open+Sans:wght@400;600;700&display=swap">
<style>
  :root {
    --bg: #e4e6ec;
    --card: #f1f1ef;
    --blue: #1d9bd8;
    --navy: #3a2c8e;
    --ink: #4a4a50;
    --rule: #9fcbe6;
  }
  * { box-sizing: border-box; margin: 0; padding: 0; }
  html, body { width: 1200px; height: 857px; overflow: hidden; }
  body {
    background: var(--bg);
    font-family: "Open Sans", Arial, sans-serif;
    position: relative;
  }
  .card {
    position: absolute;
    top: 270px;
    width: 540px;
    height: 309px;
    background: var(--card);
    overflow: hidden;
    box-shadow: 0 2px 6px rgba(40, 40, 60, 0.18);
  }
  .card--front { left: 45px; }
  .card--back { left: 615px; }

  .brand {
    position: absolute;
    display: flex;
    align-items: center;
    gap: 12px;
  }
  .brand__dot {
    width: 26px; height: 26px;
    border-radius: 50%;
    background: var(--navy);
  }
  .brand__rule { width: 1px; height: 44px; background: var(--rule); }
  .brand__name {
    font-size: 17px;
    font-weight: 600;
    color: var(--blue);
    line-height: 1.15;
    letter-spacing: 0.02em;
  }
  .card--front .brand { left: 42px; top: 42px; }
  .card--back .brand { right: 40px; top: 42px; }

  .accent {
    position: absolute;
    top: 34px;
    width: 240px; height: 240px;
    border-radius: 50%;
    background: var(--blue);
  }
  .card--front .accent { right: -120px; }
  .card--back .accent { left: -120px; }

  .person { position: absolute; left: 42px; top: 168px; }
  .person__name {
    font-size: 17px; font-weight: 700;
    color: var(--blue); letter-spacing: 0.04em;
  }
  .person__title {
    font-size: 11.5px; color: var(--ink);
    letter-spacing: 0.04em; margin-top: 1px;
  }
  .contact {
    list-style: none;
    margin-top: 20px;
    font-size: 12px; line-height: 1.45; color: var(--ink);
  }
  .contact__label { color: var(--blue); font-weight: 700; }

  .address {
    position: absolute;
    right: 40px; bottom: 52px;
    text-align: right;
    font-style: normal;
    font-size: 12px; line-height: 1.45; color: var(--ink);
  }
</style>
</head>
<body>
  <section class="card card--front" aria-label="Business card front">
    <div class="brand">
      <span class="brand__dot"></span>
      <span class="brand__rule"></span>
      <span class="brand__name">KT Holloway<br>Insurance Group</span>
    </div>
    <div class="accent"></div>
    <div class="person">
      <p class="person__name">KYLE HOLLOWAY</p>
      <p class="person__title">ACCOUNT EXECUTIVE</p>
      <ul class="contact">
        <li><span class="contact__label">T:</span> 555.201.0142 · <span class="contact__label">F:</span> 555.201.0147</li>
        <li><span class="contact__label">E:</span> kyle@kthollowayinsurance.com</li>
        <li><span class="contact__label">W:</span> www.kthollowayinsurance.com</li>
      </ul>
    </div>
  </section>

  <section class="card card--back" aria-label="Business card back">
    <div class="accent"></div>
    <div class="brand">
      <span class="brand__dot"></span>
      <span class="brand__rule"></span>
      <span class="brand__name">KT Holloway<br>Insurance Group</span>
    </div>
    <address class="address">
      28 Larimer Plaza, 1520 Blake Street<br>
      Suite 300, Aldenwood, CO 80999
    </address>
  </section>
</body>
</html>
```